Clear Road Rentals flyer

Need a A6 size horizontal layout flyer. See attached example for ideas as well as some images I have which you can use. we are a hire car company that provides vehicles to clients who have recently been involved in car accidents and who's cars are currently getting fixed and so they lose the use of their own vehicle. see our website to keep flyer in line with website and for any further information clearroadrentals.com.au

Target Market(s)

people involved in not at fault car accidents

Industry/Entity Type

It Company

Requirements
Must have
• *ask people to let us know where they got our flyer from when they call us
• *call to action for people to call our phone number 1800 452 817
Should not have
• any mentioning that the vehicle is free

```html
<!DOCTYPE html>
<html lang="en">
<head>
<meta charset="utf-8">
<title>Clear Road Rentals – A6 Flyer</title>
<link rel="stylesheet" href="https://fonts.googleapis.com/css2?family=Montserrat:wght@600;700&family=Roboto:wght@400;500;700&family=Roboto+Condensed:wght@400;700&display=swap">
<style>
  :root {
    --page-bg: #e9edf2;
    --brand-blue: #2e8ff0;
    --deep-blue: #1565d8;
    --photo-blue-dark: #1a4fd0;
    --photo-blue-light: #8fb8ef;
    --photo-warm-dark: #5a5e66;
    --photo-warm-light: #c9c2b8;
    --ink: #2b2b2b;
    --ink-soft: #444;
    --black: #0b0b0b;
    --white: #ffffff;
    --panel-light: #f7f8f9;
    --panel-grey: #e6e8ea;
    --box-line: #3a3a3a;
  }
  * { box-sizing: border-box; margin: 0; padding: 0; }
  html, body { width: 880px; height: 1200px; overflow: hidden; background: var(--page-bg); }
  body { display: flex; align-items: center; justify-content: center; font-family: "Roboto", Arial, sans-serif; }

  .flyer {
    position: relative;
    width: 818px; height: 580px;
    overflow: hidden;
    background: linear-gradient(160deg, var(--panel-light) 0%, var(--white) 45%, var(--panel-grey) 100%);
    box-shadow: 0 6px 18px rgba(0,0,0,.25);
  }

  .hero { position: absolute; left: 0; top: 0; width: 818px; height: 245px; }

  .brand-banner {
    position: absolute; left: 0; top: 0; width: 818px; height: 300px; pointer-events: none;
  }
  .brand-name {
    position: absolute; left: 195px; width: 430px; top: 258px;
    text-align: center; color: var(--white);
    font-family: "Montserrat", Arial, sans-serif; font-weight: 700; font-size: 22px;
    display: flex; align-items: center; justify-content: center; gap: 10px;
  }
  .brand-dot { width: 14px; height: 14px; border-radius: 50%; background: var(--brand-blue); }

  .headline { position: absolute; left: 33px; top: 321px; font-family: "Montserrat", Arial, sans-serif; font-weight: 700; font-size: 14px; letter-spacing: .3px; line-height: 19px; }
  .headline-accent { color: var(--deep-blue); display: block; }
  .headline-sub { color: var(--ink); display: block; }

  .step {
    position: absolute; top: 406px; width: 137px; height: 128px;
    border: 1.5px solid var(--box-line); background: rgba(255,255,255,.6);
    text-align: center; color: var(--ink-soft); font-size: 14px; line-height: 18px; letter-spacing: .2px;
    padding-top: 24px; display: flex; flex-direction: column; justify-content: center;
  }
  .step-call { left: 32px; }
  .step-details { left: 215px; }
  .step-vehicle { left: 395px; }
  .step-phone { font-weight: 700; font-size: 17px; line-height: 21px; color: var(--ink); }
  .step-icon { position: absolute; left: 50%; top: -29px; margin-left: -29px; width: 58px; height: 58px; }

  .step-arrow { position: absolute; top: 452px; width: 32px; height: 36px; }
  .arrow-one { left: 176px; }
  .arrow-two { left: 356px; }

  .referral-note {
    position: absolute; left: 33px; top: 540px; width: 520px;
    font-size: 12px; line-height: 14px; color: var(--ink-soft); font-style: normal;
  }
  .referral-note strong { color: var(--deep-blue); font-weight: 700; }

  .offer { position: absolute; left: 580px; top: 310px; width: 212px; height: 236px; }
  .offer-card {
    position: absolute; inset: 0; background: var(--brand-blue);
    clip-path: polygon(0 0,100% 0,100% 86%,80% 100%,0 100%);
  }
  .offer-curl { position: absolute; right: 0; bottom: 0; width: 44px; height: 34px; }
  .offer-frame {
    position: absolute; left: 7px; top: 10px; width: 198px; height: 142px;
    border: 1.5px solid var(--white); color: var(--white); text-align: center;
    font-family: "Roboto Condensed", Arial, sans-serif;
  }
  .offer-title { font-size: 25px; margin-top: 12px; letter-spacing: .3px; }
  .offer-figure { font-size: 58px; font-weight: 700; line-height: 56px; letter-spacing: -1px; }
  .offer-figure sup { font-size: 26px; vertical-align: 24px; margin-left: 4px; }
  .offer-period { font-size: 19px; letter-spacing: .4px; }
  .offer-perks { position: absolute; left: 12px; top: 158px; list-style: none; color: var(--white); font-weight: 700; font-size: 13px; line-height: 22px; }
  .offer-perks li::before { content: "•"; margin-right: 6px; }

  .footer-bar { position: absolute; left: 0; bottom: 0; width: 818px; height: 20px; }
</style>
</head>
<body>
  <main class="flyer">
    <svg class="hero" viewBox="0 0 818 245">
      <defs>
        <linearGradient id="carPhoto" x1="0" y1="0" x2="1" y2="1">
          <stop offset="0" stop-color="var(--photo-blue-dark)"/>
          <stop offset=".55" stop-color="var(--photo-blue-light)"/>
          <stop offset="1" stop-color="var(--photo-blue-dark)"/>
        </linearGradient>
        <linearGradient id="driverPhoto" x1="0" y1="0" x2="1" y2="1">
          <stop offset="0" stop-color="var(--photo-warm-dark)"/>
          <stop offset=".5" stop-color="var(--photo-warm-light)"/>
          <stop offset="1" stop-color="var(--photo-warm-dark)"/>
        </linearGradient>
      </defs>
      <polygon points="0,0 430,0 350,245 0,245" fill="url(#carPhoto)" role="img" aria-label="Blue-toned photo of a car front on a tree-lined road"/>
      <polygon points="430,0 818,0 818,245 350,245" fill="url(#driverPhoto)" role="img" aria-label="Photo of a smiling couple driving a car"/>
    </svg>

    <svg class="brand-banner" viewBox="0 0 818 300" aria-hidden="true">
      <polygon points="195,194 625,194 585,295 265,295" fill="var(--black)"/>
    </svg>
    <div class="brand-name"><span class="brand-dot"></span>Clear Road Rentals</div>

    <h1 class="headline">
      <span class="headline-accent">ARRANGING AN ACCIDENT REPLACEMENT VEHICLE</span>
      <span class="headline-sub">FOR YOURSELF IS EASY AS 1,2,3</span>
    </h1>

    <section class="step step-call">
      <svg class="step-icon" viewBox="0 0 58 58" aria-hidden="true">
        <circle cx="29" cy="29" r="28" fill="var(--brand-blue)" stroke="var(--white)" stroke-width="2"/>
        <path d="M20 18c2-1 3 0 4 2l2 4c.5 1 0 2-1 3l-1 1c1 3 4 6 7 7l1-1c1-1 2-1.5 3-1l4 2c2 1 3 2 2 4-1 3-3 4-6 3-8-2-14-8-16-16-1-3 0-6 1-8z" fill="var(--white)"/>
        <path d="M32 18a9 9 0 0 1 8 8M32 13a14 14 0 0 1 13 13" fill="none" stroke="var(--white)" stroke-width="2" stroke-linecap="round"/>
      </svg>
      <p>CALL US ON</p>
      <p class="step-phone">1800 452 817</p>
      <p>FREE CALL</p>
    </section>

    <svg class="step-arrow arrow-one" viewBox="0 0 32 36" aria-hidden="true"><polygon points="2,0 14,0 30,18 14,36 2,36 18,18" fill="var(--ink)"/></svg>

    <section class="step step-details">
      <svg class="step-icon" viewBox="0 0 58 58" aria-hidden="true">
        <circle cx="29" cy="29" r="28" fill="var(--brand-blue)" stroke="var(--white)" stroke-width="2"/>
        <rect x="18" y="15" width="20" height="27" rx="2" fill="none" stroke="var(--white)" stroke-width="2"/>
        <rect x="23" y="12" width="10" height="5" rx="1" fill="var(--white)"/>
        <path d="M22 24h12M22 29h12M22 34h7" stroke="var(--white)" stroke-width="2"/>
        <circle cx="38" cy="39" r="6" fill="var(--brand-blue)" stroke="var(--white)" stroke-width="2"/>
        <path d="M35 39l2 2 4-4" fill="none" stroke="var(--white)" stroke-width="2"/>
      </svg>
      <p>PROVIDE<br>ACCIDENT<br>DETAILS</p>
    </section>

    <svg class="step-arrow arrow-two" viewBox="0 0 32 36" aria-hidden="true"><polygon points="2,0 14,0 30,18 14,36 2,36 18,18" fill="var(--ink)"/></svg>

    <section class="step step-vehicle">
      <svg class="step-icon" viewBox="0 0 58 58" aria-hidden="true">
        <circle cx="29" cy="29" r="28" fill="var(--brand-blue)" stroke="var(--white)" stroke-width="2"/>
        <path d="M17 30l3-9c.5-1.5 1.5-2 3-2h12c1.5 0 2.5.5 3 2l3 9v9h-4v-3H21v3h-4z" fill="var(--white)"/>
        <path d="M21 28l2-6h12l2 6z" fill="var(--brand-blue)"/>
        <circle cx="22" cy="32" r="2" fill="var(--brand-blue)"/>
        <circle cx="36" cy="32" r="2" fill="var(--brand-blue)"/>
      </svg>
      <p>YOU GET A<br>REPLACEMENT<br>VEHICLE<br>WE TAKE CARE<br>OF THE REST</p>
    </section>

    <p class="referral-note"><strong>When you call,</strong> please let us know where you picked up this flyer.</p>

    <aside class="offer">
      <div class="offer-card"></div>
      <svg class="offer-curl" viewBox="0 0 44 34" aria-hidden="true"><polygon points="2,33 44,0 30,30" fill="#dfe3e8"/></svg>
      <div class="offer-frame">
        <p class="offer-title">SPECIAL OFFER</p>
        <p class="offer-figure">20%<sup>OFF</sup></p>
        <p class="offer-period">FOR THIS MONTH</p>
      </div>
      <ul class="offer-perks">
        <li>Free delivery</li>
        <li>Late Model/New vehicles</li>
      </ul>
    </aside>

    <svg class="footer-bar" viewBox="0 0 818 20" aria-hidden="true">
      <rect width="818" height="20" fill="var(--black)"/>
      <polygon points="0,0 410,0 402,20 0,20" fill="var(--brand-blue)"/>
    </svg>
  </main>
</body>
</html>
```